Door Hanger for 20% off on dry cleaning

I need a door hanger (3.5" x 8.5" with a hole for the door handle) for a 20% off sale on dry cleaning. The business is called "Suds by Maplecrest" and is a full-service laundry. The store is a laundromat that is used by self-serve customers. We also do wash-and-fold laundry and dry cleaning.

Some requirements:
* Include the logo
* Includes the address of the business:
615 South 300 West
Provo, Utah
(behind Harbor Crust Pies)
* Include some indication of our other services (wash-and-fold laundry, coin laundry, comforters cleaned)
* Offer needs to include an expiration date (say, September 30, 2014).

The door hanger should be full-color with designs for both sides.
Updates

The sale is for 20% off of Dry Cleaning - not the other services. And I'd like both sides of the hanger to mention the sale - in case it gets hung backwards on the door.

Industry/Entity Type

Dry Cleaning

```html
<!DOCTYPE html>
<html lang="en">
<head>
<meta charset="utf-8">
<title>Suds by Maplecrest — Door Hanger</title>
<link rel="stylesheet" href="https://fonts.googleapis.com/css2?family=Arimo:wght@400;700&family=Archivo+Black&display=swap">
<style>
  :root {
    --sky-top: #1a5fb8;
    --sky-mid: #5f9ad8;
    --cloud: #dfeaf5;
    --grass-light: #9fd26a;
    --grass-deep: #3f8f2a;
    --navy: #13237a;
    --royal: #1f3fa8;
    --orange: #f0512a;
    --white: #ffffff;
    --pale-blue: #a9d6f2;
    --ink: #0c0c0c;
  }
  html, body { margin: 0; padding: 0; overflow: hidden; background: #ffffff; }
  .hanger {
    position: relative;
    width: 1200px;
    height: 2913px;
    overflow: hidden;
    font-family: "Arimo", Arial, sans-serif;
  }
  .backdrop {
    position: absolute; inset: 0;
    background: linear-gradient(180deg,
      var(--sky-top) 0%, var(--sky-mid) 20%, var(--cloud) 34%,
      var(--sky-mid) 48%, #a8cfe8 60%, var(--grass-light) 68%, var(--grass-deep) 100%);
  }
  .hanger-cut { position: absolute; left: 0; top: 0; }

  .brand {
    position: absolute; left: 30px; top: 900px; width: 1140px; height: 300px;
    display: flex; align-items: center; gap: 36px;
  }
  .brand-mark { width: 300px; height: 300px; background: var(--royal); border-radius: 18px; flex: none; }
  .brand-name {
    font-family: "Arimo", Arial, sans-serif; font-weight: 700;
    font-size: 76px; color: var(--navy); line-height: 1; white-space: nowrap;
  }

  .headline { position: absolute; left: 0; top: 0; width: 1200px; margin: 0; color: var(--navy); }
  .headline span { position: absolute; font-weight: 700; line-height: 1; white-space: nowrap; transform-origin: left top; }
  .hl-full { left: 117px; top: 1284px; font-size: 204px; transform: scaleX(0.665); }
  .hl-star { left: 1085px; top: 1295px; font-size: 80px; }
  .hl-amp { left: 96px; top: 1419px; font-size: 275px; font-family: "Archivo Black", Arial, sans-serif; font-weight: 400 !important; color: var(--royal); }
  .hl-self { left: 292px; top: 1450px; font-size: 150px; transform: scaleX(0.86); }
  .hl-laundromat { left: 292px; top: 1574px; font-size: 110px; font-weight: 400 !important; transform: scaleX(1.05); }

  .coupon {
    position: absolute; left: 79px; top: 1762px; width: 1048px; height: 452px;
    background: var(--orange); border-radius: 40px;
    outline: 6px dashed var(--white); outline-offset: -22px;
    color: var(--white);
  }
  .coupon-discount {
    position: absolute; left: 40px; top: 22px;
    font-family: "Archivo Black", Arial, sans-serif; font-size: 196px; line-height: 1;
    letter-spacing: -4px; white-space: nowrap;
    text-shadow: 8px 8px 0 var(--royal);
  }
  .coupon-bang {
    position: absolute; left: 905px; top: -20px;
    font-family: "Archivo Black", Arial, sans-serif; font-size: 370px; line-height: 1;
    text-shadow: 8px 8px 0 var(--royal);
  }
  .coupon-item {
    position: absolute; left: 44px; top: 240px;
    font-family: "Archivo Black", Arial, sans-serif; font-size: 78px; line-height: 1;
    letter-spacing: 2px; white-space: nowrap;
    text-shadow: 5px 5px 0 var(--royal);
  }
  .coupon-expiry { position: absolute; left: 0; right: 0; top: 364px; text-align: center; font-size: 43px; font-weight: 700; }

  .services { position: absolute; top: 2300px; color: var(--white); }
  .services h3 { margin: 0; font-size: 58px; font-weight: 400; line-height: 1; white-space: nowrap; }
  .services h3 b { font-size: 76px; vertical-align: -14px; margin-right: 2px; }
  .services ul { margin: 10px 0 0 50px; padding: 0; list-style: none; font-size: 32px; line-height: 1.1; letter-spacing: 1px; white-space: nowrap; }
  .services li::before { content: "• "; }
  .services-full { left: 120px; }
  .services-self { left: 708px; }

  .location {
    position: absolute; left: 79px; top: 2622px; width: 1042px; height: 218px;
    background: var(--pale-blue); border-radius: 40px; text-align: center;
  }
  .location h2 { margin: 16px 0 0; font-size: 98px; font-weight: 700; color: var(--orange); line-height: 1; }
  .location-street { margin: 8px 0 0; font-size: 48px; font-weight: 700; color: var(--navy); line-height: 1; white-space: nowrap; }
  .location-note { margin: 6px 0 0; font-size: 38px; letter-spacing: 4px; color: var(--navy); line-height: 1; white-space: nowrap; }
</style>
</head>
<body>
<main class="hanger">
  <div class="backdrop" role="img" aria-label="Photo of blue sky with white clouds over a green grass field"></div>

  <svg class="hanger-cut" width="1200" height="1000" viewBox="0 0 1200 1000" aria-hidden="true">
    <circle cx="597" cy="481" r="288" fill="var(--white)" stroke="var(--ink)" stroke-width="6"/>
    <line x1="0" y1="676" x2="597" y2="481" stroke="var(--ink)" stroke-width="6"/>
  </svg>

  <div class="brand">
    <div class="brand-mark"></div>
    <div class="brand-name">Suds by Maplecrest</div>
  </div>

  <h1 class="headline">
    <span class="hl-full">FULL-SERVICE</span>
    <span class="hl-star">*</span>
    <span class="hl-amp">&amp;</span>
    <span class="hl-self">SELF-SERVE</span>
    <span class="hl-laundromat">LAUNDROMAT</span>
  </h1>

  <section class="coupon">
    <div class="coupon-discount">20% off</div>
    <div class="coupon-bang">!</div>
    <div class="coupon-item">ON DRY CLEANING</div>
    <div class="coupon-expiry">OFFER EXPIRES: SEPTEMBER 30, 2014.</div>
  </section>

  <section class="services services-full">
    <h3><b>*</b>FULL-SERVICE:</h3>
    <ul>
      <li>WASH-AND-FOLD LAUNDRY</li>
      <li>DRY CLEANING</li>
      <li>COMFORTERS</li>
    </ul>
  </section>
  <section class="services services-self">
    <h3><b>*</b>SELF-SERVE:</h3>
    <ul>
      <li>COIN LAUNDRY</li>
    </ul>
  </section>

  <section class="location">
    <h2>WHERE ARE WE?</h2>
    <p class="location-street">615 SOUTH 300 WEST, PROVO, UTAH</p>
    <p class="location-note">(BEHIND HARBOR CRUST PIES)</p>
  </section>
</main>
</body>
</html>
```